Harbor Nodeworks Pty Ltd

We are a Sydney based IT services company, providing managed services for corporate clients, established for over 10 years. Amongst our services we provide full infrastructure support, maintenance and upgrades. We also provide helpdesk/remote support and cloud services.

We were hoping to keep our original colours and our logo (Blue and Green, please visit our website www.harbornodeworks.com.au) however we are looking for a new business card design (with better resolution and finish) with multiple variation of the blue and green colour design options. Happy for alternative suggestion. ie new blue and green / grey and green / blue and grey et and please feel free to update current logo size ie large or smaller. (Attached our current logo and business card desig)

Industry/Entity Type

Business

Contact Information for Business Card

Name, Title, Address, Contract Information, Company Name and Logo.
(QR code if possible)

Colors
0455a3
33a6d7
3276b5
85acd3
85cae6
9bcb3c
add136
cadf82
e9f1ce

```html
<!DOCTYPE html>
<html lang="en">
<head>
<meta charset="utf-8">
<title>Harbor Nodeworks — Business Card</title>
<link rel="stylesheet" href="https://fonts.googleapis.com/css2?family=Exo+2:wght@400;500&display=swap">
<style>
  :root {
    --backdrop: #e6e6e3;
    --card: #ffffff;
    --brand-teal: #2b7f95;
    --brand-green: #7bbd46;
    --ink: #222428;
    --on-green: #ffffff;
  }
  * { box-sizing: border-box; margin: 0; padding: 0; }
  html, body {
    width: 1200px;
    height: 899px;
    overflow: hidden;
    background: var(--backdrop);
    font-family: "Exo 2", sans-serif;
  }
  .card {
    position: absolute;
    left: 80px;
    top: 150px;
    width: 1040px;
    height: 600px;
    background: var(--card);
    border-radius: 4px;
    box-shadow: 0 14px 40px rgba(0,0,0,0.18);
    overflow: hidden;
  }
  .card__panel {
    position: absolute;
    inset: 0;
    width: 1040px;
    height: 600px;
  }
  .brand {
    position: absolute;
    left: 70px;
    top: 150px;
    display: flex;
    align-items: center;
    gap: 22px;
  }
  .brand__square {
    width: 58px;
    height: 58px;
    background: var(--brand-green);
  }
  .brand__name {
    font-size: 64px;
    font-weight: 500;
    color: var(--brand-teal);
    letter-spacing: 0.5px;
  }
  .contact {
    position: absolute;
    left: 70px;
    top: 330px;
    color: var(--ink);
  }
  .contact__address {
    font-size: 22px;
    line-height: 30px;
    letter-spacing: 1px;
    margin-bottom: 22px;
  }
  .contact__list { list-style: none; }
  .contact__item {
    display: flex;
    align-items: center;
    gap: 14px;
    font-size: 19px;
    line-height: 32px;
    letter-spacing: 1px;
  }
  .contact__icon {
    width: 20px;
    height: 20px;
    fill: var(--brand-teal);
    flex: none;
  }
  .person {
    position: absolute;
    left: 820px;
    top: 268px;
    color: var(--on-green);
  }
  .person__name {
    font-size: 27px;
    font-weight: 500;
    letter-spacing: 2px;
    text-transform: uppercase;
  }
  .person__title {
    font-size: 17px;
    letter-spacing: 2.5px;
    text-transform: uppercase;
    margin-top: 4px;
  }
</style>
</head>
<body>
  <div class="card">
    <svg class="card__panel" viewBox="0 0 1040 600" aria-hidden="true">
      <path d="M768 0 Q 700 300 800 600 L1040 600 L1040 0 Z" fill="var(--brand-teal)"/>
      <path d="M782 0 Q 716 300 814 600 L1040 600 L1040 0 Z" fill="var(--brand-green)"/>
    </svg>

    <div class="brand">
      <div class="brand__square"></div>
      <span class="brand__name">Harbor Nodeworks</span>
    </div>

    <div class="contact">
      <p class="contact__address">Level 18, 83 Harbour Street<br>Sydney NSW</p>
      <ul class="contact__list">
        <li class="contact__item">
          <svg class="contact__icon" viewBox="0 0 24 24"><path d="M6.6 10.8a15 15 0 0 0 6.6 6.6l2.2-2.2c.3-.3.7-.4 1-.2 1.1.4 2.3.6 3.6.6.6 0 1 .4 1 1V20c0 .6-.4 1-1 1A17 17 0 0 1 3 4c0-.6.4-1 1-1h3.5c.6 0 1 .4 1 1 0 1.3.2 2.5.6 3.6.1.3 0 .7-.2 1z"/></svg>
          <span>02 9555 0142</span>
        </li>
        <li class="contact__item">
          <svg class="contact__icon" viewBox="0 0 24 24"><path d="M7 1h10a2 2 0 0 1 2 2v18a2 2 0 0 1-2 2H7a2 2 0 0 1-2-2V3a2 2 0 0 1 2-2zm0 3v14h10V4zm5 15.5a1 1 0 1 0 0 2 1 1 0 0 0 0-2z"/></svg>
          <span>0412 555 087</span>
        </li>
        <li class="contact__item">
          <svg class="contact__icon" viewBox="0 0 24 24"><path d="M7 2h8l3 3v5h1a2 2 0 0 1 2 2v8a2 2 0 0 1-2 2H5a2 2 0 0 1-2-2v-8a2 2 0 0 1 2-2h2zm2 2v6h7V6h-2V4zm-2 11v2h2v-2zm4 0v2h2v-2zm4 0v2h2v-2z"/></svg>
          <span>02 9555 0143</span>
        </li>
        <li class="contact__item">
          <svg class="contact__icon" viewBox="0 0 24 24"><path d="M2 5h20v14H2zm2 2v.5l8 5 8-5V7zm0 2.9V17h16V9.9l-8 5z"/></svg>
          <span>hello@harbornodeworks.com.au</span>
        </li>
        <li class="contact__item">
          <svg class="contact__icon" viewBox="0 0 24 24"><path d="M12 2a10 10 0 1 0 0 20 10 10 0 0 0 0-20zm6.9 6h-2.8a15 15 0 0 0-1.3-3.6A8 8 0 0 1 18.9 8zM12 4c.8 1.2 1.5 2.5 1.9 4h-3.8c.4-1.5 1.1-2.8 1.9-4zM4.3 14a8 8 0 0 1 0-4h3.3a16 16 0 0 0 0 4zm.8 2h2.8c.3 1.3.8 2.5 1.3 3.6A8 8 0 0 1 5.1 16zm2.8-8H5.1a8 8 0 0 1 4.1-3.6C8.7 5.5 8.2 6.7 7.9 8zM12 20c-.8-1.2-1.5-2.5-1.9-4h3.8c-.4 1.5-1.1 2.8-1.9 4zm2.3-6H9.7a14 14 0 0 1 0-4h4.6a14 14 0 0 1 0 4zm.5 5.6c.5-1.1 1-2.3 1.3-3.6h2.8a8 8 0 0 1-4.1 3.6zm1.6-5.6a16 16 0 0 0 0-4h3.3a8 8 0 0 1 0 4z"/></svg>
          <span>www.harbornodeworks.com.au</span>
        </li>
      </ul>
    </div>

    <div class="person">
      <p class="person__name">Daniel Whitford</p>
      <p class="person__title">Financial Advisor</p>
    </div>
  </div>
</body>
</html>
```